Lanternby Consulting Business Card Design

Business Card Design for Lanternby Consulting. Lanternby Consulting is a boutique consultancy based in Atlanta, GA., that specializes in marketing strategy, organization planning, and leadership development. We provide solutions for small businesses and startups as well as Meridex 400 companies.

http://lanternbyconsulting.example/

Target Market(s)

We provide solutions for small businesses and startups as well as Meridex 400 companies.

Industry/Entity Type

Consulting

Contact Information for Business Card

Two sided business card with priority on contact information, logo, tag line (Light the Way to Think Big, Act Bold, Grow Far)

Colors

Designer to choose colors to be used in the design.

Requirements
Must have
• contact information, logo, tag line (Light the Way to Think Big, Act Bold, Grow Far)
• Simple no over communication.
Nice to have
• I would like to see different placements of logo and creative use of both sides of the card
Should not have
• Do not put too much information on the card.

```html
<!DOCTYPE html>
<html lang="en">
<head>
<meta charset="utf-8">
<title>Lanternby Consulting Business Card</title>
<link href="https://fonts.googleapis.com/css2?family=Montserrat:wght@400;500;600&display=swap" rel="stylesheet">
<style>
  :root {
    --page: #d9d9d9;
    --card-light: #ffffff;
    --card-light-edge: #ececec;
    --card-dark: #2b2b2b;
    --ink: #1e1e1e;
    --ink-soft: #3a3a3a;
    --rule: #2a2a2a;
    --on-dark: #e6e6e6;
    --on-dark-soft: #cfcfcf;
  }
  * { box-sizing: border-box; margin: 0; padding: 0; }
  html, body { width: 1200px; height: 900px; overflow: hidden; }
  body {
    background: var(--page);
    font-family: "Montserrat", sans-serif;
    position: relative;
  }
  .card {
    position: absolute;
    left: 250px;
    width: 700px;
    height: 400px;
    border-radius: 22px;
    box-shadow: 0 10px 28px rgba(0,0,0,0.22);
    overflow: hidden;
  }
  .card--front {
    top: 40px;
    background: radial-gradient(ellipse at 60% 40%, var(--card-light) 40%, var(--card-light-edge) 100%);
    color: var(--ink);
  }
  .card--back {
    top: 460px;
    background: var(--card-dark);
    color: var(--on-dark);
    display: flex;
    flex-direction: column;
    align-items: center;
    justify-content: center;
  }
  .brand {
    display: flex;
    align-items: center;
    gap: 14px;
    font-weight: 600;
    letter-spacing: 0.5px;
    white-space: nowrap;
  }
  .brand__mark {
    width: 18px; height: 18px;
    border-radius: 50%;
    flex: none;
  }
  .card--front .brand {
    position: absolute;
    left: 48px; top: 48px;
    font-size: 34px;
    color: var(--ink);
  }
  .card--front .brand__mark { background: var(--ink); }
  .person {
    position: absolute;
    right: 48px; top: 170px;
    text-align: right;
  }
  .person__name {
    font-size: 26px;
    font-weight: 500;
    letter-spacing: 1px;
    text-transform: uppercase;
    line-height: 1.1;
  }
  .person__title {
    font-size: 15px;
    color: var(--ink-soft);
    margin-top: 4px;
  }
  .rule {
    position: absolute;
    left: 48px; right: 48px; top: 236px;
    height: 2px;
    background: var(--rule);
  }
  .address {
    position: absolute;
    right: 48px; top: 254px;
    text-align: right;
    font-size: 16px;
    line-height: 1.45;
    color: var(--ink-soft);
  }
  .contacts {
    position: absolute;
    left: 48px; bottom: 34px;
    list-style: none;
    font-size: 16px;
    line-height: 1.6;
    color: var(--ink-soft);
  }
  .contacts li { display: flex; align-items: center; gap: 12px; white-space: nowrap; }
  .contacts svg { width: 14px; height: 14px; fill: var(--ink-soft); flex: none; }
  .card--back .brand {
    font-size: 46px;
    color: var(--on-dark);
  }
  .card--back .brand__mark { background: var(--on-dark); width: 24px; height: 24px; }
  .tagline {
    margin-top: 34px;
    font-size: 20px;
    letter-spacing: 0.6px;
    color: var(--on-dark-soft);
    white-space: nowrap;
  }
</style>
</head>
<body>
  <section class="card card--front" aria-label="Card front">
    <div class="brand"><span class="brand__mark"></span>Lanternby Consulting</div>
    <div class="person">
      <p class="person__name">Daniel Rowe</p>
      <p class="person__title">Director</p>
    </div>
    <div class="rule"></div>
    <p class="address">Calle Norte 14,<br>Springvale, SV 00142</p>
    <ul class="contacts">
      <li><svg viewBox="0 0 16 16"><path d="M3 1h3l1.5 4-2 1.3a9 9 0 0 0 4.2 4.2L11 8.5l4 1.5v3a2 2 0 0 1-2 2A12 12 0 0 1 1 3a2 2 0 0 1 2-2z"/></svg>+1 404 555 0142</li>
      <li><svg viewBox="0 0 16 16"><path d="M4 0h8a1 1 0 0 1 1 1v14a1 1 0 0 1-1 1H4a1 1 0 0 1-1-1V1a1 1 0 0 1 1-1zm1 2v10h6V2zm3 11a1 1 0 1 0 0 2 1 1 0 0 0 0-2z"/></svg>+1 404 555 0187</li>
      <li><svg viewBox="0 0 16 16"><path d="M1 3h14v10H1zm1.5 1.5v.4L8 8.6l5.5-3.7v-.4zm0 2.2V11.5h11V6.7L8 10.4z"/></svg>hello@lanternby.example</li>
      <li><svg viewBox="0 0 16 16"><path d="M8 0a8 8 0 1 0 0 16A8 8 0 0 0 8 0zm-1 1.6V5H4.2A6.5 6.5 0 0 1 7 1.6zm2 0A6.5 6.5 0 0 1 11.8 5H9zM1.6 7H7v2H1.6a6.5 6.5 0 0 1 0-2zm7.4 0h5.4a6.5 6.5 0 0 1 0 2H9zM4.2 11H7v3.4A6.5 6.5 0 0 1 4.2 11zM9 11h2.8A6.5 6.5 0 0 1 9 14.4z"/></svg>www.LanternbyConsulting.example</li>
    </ul>
  </section>

  <section class="card card--back" aria-label="Card back">
    <div class="brand"><span class="brand__mark"></span>Lanternby Consulting</div>
    <p class="tagline">Light the Way to Think Big, Act Bold, Grow Far</p>
  </section>
</body>
</html>
```